Graphic Design of Business Process

We require an eye-catching, sophisticated design of 2 business processes (attached), that will be used digitally AND for print (to be put on walls in our office).

The basic layout is attached. We require a creative, professional designer to re-design these so that they look appealing but still able to grasp all the information.

We will require vector files and editable project files for final delivery. You may refer to our website (kitefieldmedia.com.au) for an indication of our brand.

If you have any questions, please ask.

Thank you.

```html
<!DOCTYPE html>
<html lang="en">
<head>
<meta charset="UTF-8">
<title>Content Hierarchy</title>
<link href="https://fonts.googleapis.com/css2?family=Montserrat:wght@600;700&display=swap" rel="stylesheet">
<style>
  :root {
    --bg-top: #d3ebf0;
    --bg-bottom: #cadbea;
    --navy: #0e4e87;
    --sky: #449dd6;
    --ink: #0a0a0a;
    --label: #ffffff;
    --hero-a: #1f4a86;
    --hero-b: #2a2a6c;
    --hub-a: #98bb3b;
    --hub-b: #6aa443;
    --hyg-a: #c6522a;
    --hyg-b: #a81f26;
  }
  html, body {
    margin: 0;
    padding: 0;
    width: 1200px;
    height: 1200px;
    overflow: hidden;
  }
  .canvas {
    position: relative;
    width: 1200px;
    height: 1200px;
    background: linear-gradient(160deg, var(--bg-top), var(--bg-bottom));
    font-family: "Montserrat", sans-serif;
  }
  .canvas svg { position: absolute; inset: 0; }
  .title {
    position: absolute;
    top: 303px;
    left: 0;
    width: 1262px;
    margin: 0;
    text-align: center;
    font-size: 37px;
    font-weight: 700;
    letter-spacing: 0.5px;
    color: var(--ink);
  }
  .tier-name { font-weight: 700; font-size: 28px; fill: var(--label); letter-spacing: 1px; }
  .tier-desc { font-weight: 700; font-size: 21px; fill: var(--label); letter-spacing: 0.6px; }
</style>
</head>
<body>
<div class="canvas">
  <svg width="1200" height="1200" viewBox="0 0 1200 1200">
    <defs>
      <linearGradient id="hero-fill" x1="0" y1="0" x2="0" y2="1">
        <stop offset="0" stop-color="var(--hero-a)"/>
        <stop offset="0.6" stop-color="#1c3d7d"/>
        <stop offset="1" stop-color="var(--hero-b)"/>
      </linearGradient>
      <linearGradient id="hub-fill" x1="0" y1="0" x2="0" y2="1">
        <stop offset="0" stop-color="var(--hub-a)"/>
        <stop offset="0.6" stop-color="#9ac13c"/>
        <stop offset="1" stop-color="var(--hub-b)"/>
      </linearGradient>
      <linearGradient id="hygiene-fill" x1="0" y1="0" x2="0" y2="1">
        <stop offset="0" stop-color="var(--hyg-a)"/>
        <stop offset="0.6" stop-color="#bd4529"/>
        <stop offset="1" stop-color="var(--hyg-b)"/>
      </linearGradient>
    </defs>

    <g class="header-swoosh">
      <path d="M653 0 H1200 V17 Q 950 45 729 82 C 752 55 720 25 653 0 Z" fill="var(--sky)"/>
      <path d="M0 0 H653 C720 25 752 55 729 82 Q 400 150 2 272 Z" fill="var(--navy)"/>
    </g>

    <g class="tier tier-hero">
      <polygon points="434,477 607,443 607,605 434,640" fill="url(#hero-fill)"/>
      <polygon points="607,443 780,477 780,640 607,605" fill="url(#hero-fill)" opacity="0.95"/>
      <text class="tier-name" x="544" y="548" text-anchor="middle">HERO</text>
      <text class="tier-desc" x="620" y="527">TENTPOLE</text>
      <text class="tier-desc" x="620" y="555">CAMPAIGNS</text>
    </g>

    <g class="tier tier-hub">
      <polygon points="342,668 607,615 607,774 342,829" fill="url(#hub-fill)"/>
      <polygon points="607,615 871,668 871,829 607,774" fill="url(#hub-fill)"/>
      <text class="tier-name" x="483" y="730" text-anchor="middle">HUB</text>
      <text class="tier-desc" x="623" y="711">REGULAR “PUSH”</text>
      <text class="tier-desc" x="623" y="739">CONTENT</text>
    </g>

    <g class="tier tier-hygiene">
      <polygon points="253,859 607,786 607,945 253,1019" fill="url(#hygiene-fill)"/>
      <polygon points="607,786 959,859 959,1019 607,945" fill="url(#hygiene-fill)" opacity="0.95"/>
      <text class="tier-name" x="444" y="911" text-anchor="middle">HYGIENE</text>
      <text class="tier-desc" x="625" y="887">ALWAYS-ON “PULL”</text>
      <text class="tier-desc" x="625" y="915">CONTENT</text>
    </g>
  </svg>
  <h1 class="title">CONTENT HIERARCHY</h1>
</div>
</body>
</html>
```